Instagram animated GIF stickers

I want to have you design roughly 5 different animated GIFs to use in Instagram stories. The GIFs will have transparent backgrounds and incorporate my logo.

Target Market(s)

Real estate

Industry/Entity Type

Real Estate Agent

Colors
33b8a4
34a6d7

Requirements
Must have
• Here is the list of how I'd like them animated:
• My logo + Under Contract
• My logo + Swipe Up
• My logo + Sold
• My logo + Elm Hollow sign outline (image attached) = ❤️
• My logo + Just Listed

```html
<!DOCTYPE html>
<html lang="en">
<head>
<meta charset="utf-8">
<title>Calder Property Experts – Story Stickers</title>
<link href="https://fonts.googleapis.com/css2?family=Jost:wght@400;500;700;800&display=swap" rel="stylesheet">
<style>
  :root {
    --ink: #1b1b1b;
    --brand-blue: #34a6d7;
    --arrow-grey: #b5b5b5;
    --tagline-grey: #9a9a9a;
    --heart-red: #e22d26;
    --sign-slate: #5e6378;
    --sign-post: #1e1e1e;
    --paper: #fdfdfd;
  }
  * { margin: 0; padding: 0; box-sizing: border-box; }
  html, body { width: 1200px; height: 2203px; overflow: hidden; }
  body {
    position: relative;
    background: var(--paper);
    font-family: "Jost", sans-serif;
    color: var(--ink);
  }
  .sticker-sheet {
    position: absolute; inset: 0;
    border: 2px solid #d8d8d8;
  }

  /* Brand lockup */
  .brand {
    position: absolute;
    width: 300px;
    text-align: center;
  }
  .brand-square {
    width: 134px; height: 134px;
    margin: 0 auto;
    border: 8px solid var(--ink);
  }
  .brand-name {
    margin-top: 14px;
    font-size: 66px;
    font-weight: 500;
    letter-spacing: 4px;
    line-height: 1;
  }
  .brand-tagline {
    margin-top: 10px;
    font-size: 21px;
    font-weight: 400;
    color: var(--tagline-grey);
    letter-spacing: 0.5px;
  }

  /* Shapes */
  .shape { position: absolute; overflow: visible; }

  /* Sticker captions */
  .caption {
    position: absolute;
    font-weight: 800;
    text-align: center;
    line-height: 1;
    color: var(--ink);
  }
  .caption-contract { left: 805px; top: 218px; width: 300px; font-size: 40px; letter-spacing: 1px; }
  .caption-contract span { display: block; margin-bottom: 2px; }
  .caption-swipe { left: 815px; top: 556px; width: 300px; font-size: 48px; letter-spacing: 1px; }
  .caption-listed { left: 814px; top: 1182px; width: 300px; font-size: 46px; }
  .caption-listed span { display: block; }
  .caption-sold {
    left: 840px; top: 805px; width: 254px; height: 86px;
    display: flex; align-items: center; justify-content: center;
    font-size: 70px; padding-top: 2px;
  }

  .neighbourhood-sign {
    position: absolute;
    left: 899px; top: 1851px;
    width: 141px; height: 223px;
  }
  .neighbourhood-sign .post {
    position: absolute; right: 0; top: 0;
    width: 22px; height: 223px;
    background: var(--sign-post);
  }
  .neighbourhood-sign .panel {
    position: absolute; left: 0; top: 48px;
    width: 120px; height: 160px;
    background: linear-gradient(180deg, #6a6f84, var(--sign-slate) 60%, #4d5163);
  }
</style>
</head>
<body>
<main class="sticker-sheet">

  <!-- Under contract -->
  <div class="brand" style="left:423px; top:91px;">
    <div class="brand-square"></div>
    <div class="brand-name">CALDER</div>
    <div class="brand-tagline">PROPERTY EXPERTS</div>
  </div>
  <svg class="shape" style="left:779px; top:137px;" width="34" height="64"><polygon points="0,0 32,32 0,64" fill="var(--arrow-grey)"/></svg>
  <svg class="shape contract-icon" style="left:911px; top:91px;" width="130" height="120" viewBox="0 0 130 120">
    <path d="M4 4 H68 L90 26 V112 H4 Z" fill="var(--brand-blue)" stroke="var(--ink)" stroke-width="3"/>
    <path d="M14 14 H64 L80 30 V102 H14 Z" fill="#fff" stroke="var(--ink)" stroke-width="2"/>
    <g stroke="var(--brand-blue)" stroke-width="5">
      <line x1="24" y1="40" x2="66" y2="40"/><line x1="24" y1="54" x2="66" y2="54"/>
      <line x1="24" y1="68" x2="60" y2="68"/><line x1="24" y1="82" x2="50" y2="82"/>
    </g>
    <g transform="rotate(40 100 60)">
      <rect x="92" y="10" width="18" height="80" fill="var(--brand-blue)" stroke="var(--ink)" stroke-width="3"/>
      <polygon points="92,90 110,90 101,110" fill="#fff" stroke="var(--ink)" stroke-width="3"/>
    </g>
  </svg>
  <div class="caption caption-contract"><span>UNDER</span><span>CONTRACT</span></div>

  <!-- Swipe up -->
  <div class="brand" style="left:430px; top:398px;">
    <div class="brand-square"></div>
    <div class="brand-name">CALDER</div>
    <div class="brand-tagline">PROPERTY EXPERTS</div>
  </div>
  <svg class="shape" style="left:763px; top:435px;" width="34" height="64"><polygon points="0,0 32,32 0,64" fill="var(--arrow-grey)"/></svg>
  <svg class="shape swipe-icon" style="left:903px; top:383px;" width="106" height="150" viewBox="0 0 106 150">
    <path d="M34 92 V14 a9 9 0 0 1 18 0 V62 H88 a12 12 0 0 1 12 12 V112 L84 132 H40 L8 92 a9 9 0 0 1 14 -10 Z" fill="#fff" stroke="var(--brand-blue)" stroke-width="6" stroke-linejoin="round"/>
    <path d="M34 92 V14 a9 9 0 0 1 18 0 V62 H88 a12 12 0 0 1 12 12 V112 L84 132 H40 L8 92 a9 9 0 0 1 14 -10 Z" fill="none" stroke="var(--ink)" stroke-width="2" stroke-linejoin="round"/>
    <rect x="40" y="132" width="50" height="14" fill="var(--brand-blue)" stroke="var(--ink)" stroke-width="2"/>
  </svg>
  <div class="caption caption-swipe">SWIPE UP</div>

  <!-- Sold -->
  <div class="brand" style="left:430px; top:711px;">
    <div class="brand-square"></div>
    <div class="brand-name">CALDER</div>
    <div class="brand-tagline">PROPERTY EXPERTS</div>
  </div>
  <svg class="shape" style="left:761px; top:754px;" width="34" height="64"><polygon points="0,0 32,32 0,64" fill="var(--arrow-grey)"/></svg>
  <svg class="shape sold-sign" style="left:840px; top:735px;" width="254" height="160" viewBox="0 0 254 160">
    <polyline points="85,70 126,24 167,70" fill="none" stroke="var(--ink)" stroke-width="4"/>
    <circle cx="126" cy="20" r="12" fill="var(--brand-blue)" stroke="var(--ink)" stroke-width="3"/>
    <path d="M2 70 H250 V100 a12 12 0 0 0 0 24 V156 H2 V124 a12 12 0 0 0 0 -24 Z" fill="var(--brand-blue)" stroke="var(--ink)" stroke-width="3"/>
    <path d="M12 80 H240 V96 a16 16 0 0 0 0 32 V146 H12 V128 a16 16 0 0 0 0 -32 Z" fill="#fff" stroke="var(--ink)" stroke-width="2"/>
  </svg>
  <div class="caption caption-sold">SOLD</div>

  <!-- Just listed -->
  <div class="brand" style="left:420px; top:1074px;">
    <div class="brand-square"></div>
    <div class="brand-name">CALDER</div>
    <div class="brand-tagline">PROPERTY EXPERTS</div>
  </div>
  <svg class="shape" style="left:779px; top:1111px;" width="34" height="64"><polygon points="0,0 32,32 0,64" fill="var(--arrow-grey)"/></svg>
  <svg class="shape listed-icon" style="left:922px; top:1052px;" width="140" height="112" viewBox="0 0 156 124">
    <rect x="2" y="2" width="100" height="118" rx="6" fill="var(--brand-blue)" stroke="var(--ink)" stroke-width="3"/>
    <g stroke="var(--ink)" stroke-width="5">
      <line x1="18" y1="30" x2="84" y2="30"/><line x1="18" y1="48" x2="84" y2="48"/>
      <line x1="18" y1="66" x2="70" y2="66"/><line x1="18" y1="84" x2="60" y2="84"/>
    </g>
    <polyline points="84,50 106,72 148,22" fill="none" stroke="var(--ink)" stroke-width="22" stroke-linejoin="round"/>
    <polyline points="84,50 106,72 148,22" fill="none" stroke="var(--brand-blue)" stroke-width="15" stroke-linejoin="round"/>
  </svg>
  <div class="caption caption-listed"><span>JUST</span><span>LISTED</span></div>

  <!-- Neighbourhood equation -->
  <div class="brand" style="left:427px; top:1532px;">
    <div class="brand-square"></div>
    <div class="brand-name">CALDER</div>
    <div class="brand-tagline">PROPERTY EXPERTS</div>
  </div>
  <svg class="shape" style="left:761px; top:1588px;" width="34" height="64"><polygon points="0,0 32,32 0,64" fill="var(--arrow-grey)"/></svg>
  <svg class="shape plus-sign" style="left:855px; top:1542px;" width="182" height="188" viewBox="0 0 182 188">
    <path d="M72 1 H110 V73 H181 V113 H110 V187 H72 V113 H1 V73 H72 Z" fill="var(--brand-blue)" stroke="var(--ink)" stroke-width="1.5"/>
  </svg>
  <svg class="shape" style="left:918px; top:1763px;" width="64" height="34"><polygon points="0,0 64,0 32,32" fill="var(--arrow-grey)"/></svg>

  <div class="neighbourhood-sign" role="img" aria-label="Photo of the Elm Hollow historic district street sign hanging from a black post">
    <div class="panel"></div>
    <div class="post"></div>
  </div>

  <svg class="shape" style="left:771px; top:1976px;" width="34" height="66"><polygon points="32,0 0,33 32,66" fill="var(--arrow-grey)"/></svg>
  <svg class="shape equals-sign" style="left:510px; top:1958px;" width="142" height="100" viewBox="0 0 142 100">
    <rect x="1" y="1" width="140" height="32" fill="var(--brand-blue)" stroke="var(--ink)" stroke-width="1.5"/>
    <rect x="1" y="67" width="140" height="32" fill="var(--brand-blue)" stroke="var(--ink)" stroke-width="1.5"/>
  </svg>
  <svg class="shape" style="left:394px; top:1976px;" width="34" height="66"><polygon points="32,0 0,33 32,66" fill="var(--arrow-grey)"/></svg>
  <svg class="shape heart" style="left:116px; top:1950px;" width="170" height="140" viewBox="0 0 170 140">
    <path d="M85 136 C60 112 4 82 4 42 C4 18 22 4 42 4 C62 4 78 16 85 32 C92 16 108 4 128 4 C148 4 166 18 166 42 C166 82 110 112 85 136 Z" fill="var(--heart-red)" stroke="var(--ink)" stroke-width="3"/>
  </svg>

</main>
</body>
</html>
```